Admin Backend Redesign

We need a redesign for our backend which supoosed to make the backoffice look more modern!

I will add screenshots of the backoffice so you know what data will be shown in the Admin.

Have in mind that the users of this backend are Doctors. We need a clinical look, modern and sharp. The backoffice is responsive, have that in mind. We need the backoffice to look as professional as possible.

The theme used for the website is: http://velmora.quillstack-sample.com/

ON the main page of the backoffice, under every widget i need some space to write an explanation what the widget is about.

The color code used in our logo and website is #57aad4 combined with white.

We are open for ideas!
Updates

Project Deadline Extended
Reason: Designs are ok, but nothing innovative. Please use more modern designs!

Project Deadline Extended
Reason: Havent recieved a perfect design yet. Please read instructions carefully! Thank you

Project Deadline Extended
Reason: Hey everybody, sorry for the delay. We will decide in 3 days. If anyone wants to add a Design, that would be great.

Target Market(s)

Doctors, therapists

Industry/Entity Type

It Professional

Font styles to use
Sans Serif

Requirements
Must have
• Must look uptodate, modern, like new back offices look nowadays

```html
<!DOCTYPE html>
<html lang="de">
<head>
<meta charset="utf-8">
<title>Praxis Backend – Dashboard</title>
<link rel="stylesheet" href="https://fonts.googleapis.com/css2?family=Open+Sans:wght@400;600&display=swap">
<style>
:root{
  --page:#4e5b63;
  --topbar:#46535b;
  --card:#289cd8;
  --card-head:#0b88c9;
  --nav-item:#0b88c9;
  --nav-active:#289cd8;
  --white:#ffffff;
  --search:#c9e0ec;
  --search-text:#3f8fb8;
  --pager:#e0f1fa;
  --ok:#23c4b8;
  --pie-yellow:#fedb80;
  --pie-cyan:#94f2ee;
  --pie-red:#f98680;
  --pie-grey:#dcdcdc;
  --pie-purple:#c883ee;
}
*{box-sizing:border-box;margin:0;padding:0}
html,body{width:960px;height:1200px;overflow:hidden}
body{background:var(--page);font-family:"Open Sans",sans-serif;color:var(--white);position:relative}
.topbar{position:absolute;left:0;top:0;width:960px;height:42px;background:var(--topbar);border-bottom:1px solid #3e4a51}
.user{position:absolute;left:786px;top:7px;display:flex;align-items:center;gap:5px;font-size:12px}
.avatar{width:26px;height:26px;background:linear-gradient(#e9e4de,#b9c4cc)}
.caret{width:0;height:0;border-left:4px solid transparent;border-right:4px solid transparent;border-top:7px solid var(--white);margin-left:6px}
.sidenav{position:absolute;left:88px;top:54px;width:172px}
.nav-item{height:36px;background:var(--nav-item);display:flex;align-items:center;font-size:12px;padding-left:9px;gap:10px;border-bottom:1px solid #2a95cd}
.nav-item.active{background:var(--nav-active)}
.nav-item svg{width:20px;height:20px;fill:var(--white)}
.card{position:absolute;background:var(--card);width:283px}
.card-head{height:31px;background:var(--card-head);font-size:11.5px;display:flex;align-items:center;padding-left:14px;gap:10px}
.hero{height:109px}
.hero-body{height:76px;display:flex;align-items:center;padding-left:18px;gap:22px;border-bottom:1px solid #4eaee0}
.hero-body svg{width:46px;height:48px;fill:var(--white)}
.hero-title{font-size:24px;line-height:1.05}
.hero-sub{font-size:14.5px;color:#e4f3fb}
.hero-link{height:33px;display:flex;align-items:center;justify-content:space-between;padding:0 10px 0 11px;font-size:13px;text-transform:uppercase}
.welcome-body{padding:11px 12px;font-size:11px;line-height:13px}
.welcome-body p+p{margin-top:10px}
.btn-ok{display:block;margin:9px 0 0 -2px;width:107px;height:30px;background:var(--ok);border:1px solid #1ea89e;font-size:11.5px;text-align:center;line-height:28px}
.axis{font-size:8.5px;fill:var(--white);font-family:"Open Sans",sans-serif}
.legend{position:absolute;left:200px;top:58px;font-size:11.5px;line-height:17.6px}
.legend span{display:inline-block;width:9px;height:9px;margin-right:6px;vertical-align:-1px}
.search{position:absolute;left:9px;top:41px;width:265px;height:24px;background:var(--search);color:var(--search-text);font-size:9.5px;padding-left:9px;line-height:24px}
.search svg{position:absolute;right:8px;top:5px;width:14px;height:14px}
.table{position:absolute;left:0;top:73px;width:283px}
.thead{position:relative;height:25px;margin:0 13px;border-bottom:1px solid #bfe3f5;font-size:11.5px}
.thead span,.row span{position:absolute;white-space:nowrap}
.thead span{top:4px}
.sort{display:inline-block;width:4px;height:7px;margin-right:3px;vertical-align:0}
.rows{position:relative;margin-top:12px}
.row{position:relative;height:18.4px;font-size:9.6px}
.bar{display:inline-block;height:8px;background:var(--white);margin-top:2px}
.foot{position:absolute;left:12px;bottom:9px;right:13px;display:flex;justify-content:space-between;align-items:center;font-size:11.5px}
.pager{display:flex;gap:1px}
.pager span{width:15px;height:15px;background:var(--pager);color:var(--card);font-size:9px;text-align:center;line-height:15px;display:flex;align-items:center;justify-content:center}
.pager span.arrow{width:16px}
.stars{letter-spacing:0.5px;font-size:8px}
</style>
</head>
<body>
<header class="topbar">
  <div class="user">
    <div class="avatar" role="img" aria-label="Profilfoto des Arztes"></div>
    <span>Dr.</span><span class="caret"></span>
  </div>
</header>

<nav class="sidenav">
  <div class="nav-item active"><svg viewBox="0 0 20 20"><path d="M10 2 1 10h3v8h5v-5h2v5h5v-8h3z"/></svg>Dashboard</div>
  <div class="nav-item"><svg viewBox="0 0 20 20"><circle cx="10" cy="5" r="4"/><path d="M3 19c0-6 3-8 7-8s7 2 7 8z"/></svg>Mien Konto</div>
  <div class="nav-item"><svg viewBox="0 0 20 20"><circle cx="10" cy="5" r="4"/><path d="M3 19c0-6 3-8 7-8s7 2 7 8z"/></svg>Patientenbewertungen</div>
</nav>

<section class="card hero" style="left:275px;top:54px">
  <div class="hero-body">
    <svg viewBox="0 0 46 48"><circle cx="23" cy="12" r="10"/><path d="M3 48c0-16 8-23 20-23s20 7 20 23z"/><path d="M14 28v8a9 9 0 0 0 18 0" stroke="#289cd8" stroke-width="2" fill="none"/><circle cx="32" cy="36" r="3" fill="#289cd8"/></svg>
    <div><div class="hero-title">Profil</div><div class="hero-sub">Profile bearbeiten</div></div>
  </div>
  <div class="hero-link"><span>Weiter</span><svg width="16" height="12" viewBox="0 0 16 12"><path d="M0 6h14M9 1l5 5-5 5" stroke="#fff" stroke-width="2" fill="none"/></svg></div>
</section>

<section class="card hero" style="left:574px;top:54px">
  <div class="hero-body">
    <svg viewBox="0 0 46 48"><circle cx="23" cy="12" r="10"/><path d="M3 48c0-16 8-23 20-23s20 7 20 23z"/><rect x="10" y="34" width="16" height="9" fill="#289cd8"/></svg>
    <div><div class="hero-title">Patienten</div><div class="hero-sub">Patienten verwalten</div></div>
  </div>
  <div class="hero-link"><span>Alle ansehen</span><svg width="16" height="12" viewBox="0 0 16 12"><path d="M0 6h14M9 1l5 5-5 5" stroke="#fff" stroke-width="2" fill="none"/></svg></div>
</section>

<section class="card" style="left:275px;top:179px;height:167px">
  <div class="card-head"><svg width="20" height="15" viewBox="0 0 20 15"><rect x="0.5" y="0.5" width="19" height="14" fill="#fff"/><path d="M2 13l5-6 4 4 3-3 4 5z" fill="#0b88c9"/><circle cx="14" cy="4" r="1.6" fill="#0b88c9"/></svg>Willkommen: Dr. Mustermann</div>
  <div class="welcome-body">
    <p>Der Status Ihres offentlichen Profils ist derzeit:</p>
    <p>Lorem ipsum dolor sit amet, consectetur adipisicing elit, sed do eiusmod tempor incididunt ut labore et dolore magna aliqua. Ut enim ad minim veniam,</p>
    <span class="btn-ok">Alles OK</span>
  </div>
</section>

<section class="card" style="left:574px;top:179px;height:167px">
  <div class="card-head" style="padding-left:17px">Rankora Trend fur:</div>
  <svg width="283" height="136" viewBox="0 31 283 136" style="display:block">
    <path d="M24 46V143H265" stroke="#fff" stroke-width="1" fill="none"/>
    <text class="axis" x="20" y="49" text-anchor="end">15</text>
    <text class="axis" x="20" y="83" text-anchor="end">10</text>
    <text class="axis" x="20" y="113" text-anchor="end">5</text>
    <text class="axis" x="20" y="146" text-anchor="end">0</text>
    <g text-anchor="middle"><text class="axis" x="50" y="159">Oct 2012</text><text class="axis" x="99" y="159">Jan 2013</text><text class="axis" x="150" y="159">Apr 2013</text><text class="axis" x="198" y="159">Jul 2013</text><text class="axis" x="246" y="159">Oct 2013</text></g>
    <polyline fill="none" stroke="#fff" stroke-width="1" points="98.4,143.2 106.4,92.8 116,80.8 120.8,90.4 127.2,87.2 133.6,41.6 140,52.8 152.8,104.8 167.2,112.8 175.2,98.4 188,118.4 199.2,91.2 207.2,99.2 221.6,87.2 232.8,92.8 238.4,85.6 244,92.8 248.8,86.4 261.6,85.6"/>
  </svg>
</section>

<section class="card" style="left:275px;top:362px;height:226px">
  <div class="card-head">Pie 1</div>
  <svg width="283" height="195" viewBox="0 31 283 195" style="position:absolute;left:0;top:31px">
    <path d="M94 124L94 50A74 74 0 0 1 111.9 195.8Z" fill="var(--pie-yellow)"/>
    <path d="M94 124L111.9 195.8A74 74 0 0 1 48.4 182.3Z" fill="var(--pie-cyan)"/>
    <path d="M94 124L48.4 182.3A74 74 0 0 1 94 50Z" fill="var(--pie-red)"/>
  </svg>
  <div class="legend">
    <div><span style="background:var(--pie-yellow)"></span>Series 1</div>
    <div><span style="background:var(--pie-cyan)"></span>Series 2</div>
    <div><span style="background:var(--pie-red)"></span>Series 3</div>
  </div>
</section>

<section class="card" style="left:574px;top:362px;height:226px">
  <div class="card-head">Pie 2</div>
  <svg width="283" height="195" viewBox="0 31 283 195" style="position:absolute;left:0;top:31px">
    <path d="M93 124L93 50A74 74 0 0 1 109.6 51.9Z" fill="var(--pie-yellow)"/>
    <path d="M93 124L109.6 51.9A74 74 0 0 1 157.1 87Z" fill="var(--pie-cyan)"/>
    <path d="M93 124L157.1 87A74 74 0 0 1 110.9 195.8Z" fill="var(--pie-red)"/>
    <path d="M93 124L110.9 195.8A74 74 0 0 1 47.4 182.3Z" fill="var(--pie-grey)"/>
    <path d="M93 124L47.4 182.3A74 74 0 0 1 93 50Z" fill="var(--pie-purple)"/>
  </svg>
  <div class="legend">
    <div><span style="background:var(--pie-yellow)"></span>Series 1</div>
    <div><span style="background:var(--pie-cyan)"></span>Series 2</div>
    <div><span style="background:var(--pie-red)"></span>Series 3</div>
    <div><span style="background:var(--pie-grey)"></span>Series 5</div>
    <div><span style="background:var(--pie-purple)"></span>Series 6</div>
  </div>
</section>

<section class="card" style="left:275px;top:604px;height:246px">
  <div class="card-head">Stat 1</div>
  <div class="search">search<svg viewBox="0 0 14 14"><circle cx="5.5" cy="5.5" r="4.3" stroke="#2a8fc4" stroke-width="2" fill="none"/><path d="M8.7 8.7l4 4" stroke="#2a8fc4" stroke-width="2.4"/></svg></div>
  <div class="table">
    <div class="thead"><span style="left:0">Name</span><span style="left:56px"><svg class="sort" viewBox="0 0 4 7"><path d="M0 3 2 0 4 3zM0 4 2 7 4 4z" fill="#fff"/></svg>Position</span><span style="left:121px"><svg class="sort" viewBox="0 0 4 7"><path d="M0 3 2 0 4 3zM0 4 2 7 4 4z" fill="#fff"/></svg>Start Date</span><span style="left:200px"><svg class="sort" viewBox="0 0 4 7"><path d="M0 3 2 0 4 3zM0 4 2 7 4 4z" fill="#fff"/></svg>Salary</span></div>
    <div class="rows">
      <div class="row"><span style="left:13px">Gerdan</span><span style="left:76px">Chefin</span><span style="left:145px">1.11.2013</span><span style="left:223px">Salami</span></div>
      <div class="row"><span style="left:13px">Gerdan</span><span style="left:76px">Chefin</span><span style="left:145px">1.11.2013</span><span style="left:223px">Salami</span></div>
      <div class="row"><span style="left:13px">Gerdan</span><span style="left:76px">Chefin</span><span style="left:145px">1.11.2013</span><span style="left:223px">Salami</span></div>
      <div class="row"><span style="left:13px">Gerdan</span><span style="left:76px">Chefin</span><span style="left:145px">1.11.2013</span><span style="left:223px">Salami</span></div>
      <div class="row"><span style="left:13px">Gerdan</span><span style="left:76px">Chefin</span><span style="left:145px">1.11.2013</span><span style="left:223px">Salami</span></div>
    </div>
  </div>
  <div class="foot"><span>Showing 1 to 5 of 9 entries</span><div class="pager"><span class="arrow"><svg width="9" height="7" viewBox="0 0 9 7"><path d="M9 3.5H1M4 0.5 1 3.5l3 3" stroke="#289cd8" stroke-width="1.2" fill="none"/></svg></span><span>1</span><span>2</span><span class="arrow"><svg width="9" height="7" viewBox="0 0 9 7"><path d="M0 3.5h8M5 0.5l3 3-3 3" stroke="#289cd8" stroke-width="1.2" fill="none"/></svg></span></div></div>
</section>

<section class="card" style="left:574px;top:604px;height:246px">
  <div class="card-head">Stat 2</div>
  <div class="search">search<svg viewBox="0 0 14 14"><circle cx="5.5" cy="5.5" r="4.3" stroke="#2a8fc4" stroke-width="2" fill="none"/><path d="M8.7 8.7l4 4" stroke="#2a8fc4" stroke-width="2.4"/></svg></div>
  <div class="table">
    <div class="thead"><span style="left:0">Domain</span><span style="left:56px"><svg class="sort" viewBox="0 0 4 7"><path d="M0 3 2 0 4 3zM0 4 2 7 4 4z" fill="#fff"/></svg>Niveau</span><span style="left:121px"><svg class="sort" viewBox="0 0 4 7"><path d="M0 3 2 0 4 3zM0 4 2 7 4 4z" fill="#fff"/></svg>Keyw.</span><span style="left:202px"><svg class="sort" viewBox="0 0 4 7"><path d="M0 3 2 0 4 3zM0 4 2 7 4 4z" fill="#fff"/></svg>Seyw.</span></div>
    <div class="rows">
      <div class="row"><span style="left:13px">domain1.de</span><span style="left:78px"><i class="bar" style="width:7px"></i></span><span style="left:136px">Gemeinsame K</span><span style="left:221px">SE Keyw</span></div>
      <div class="row"><span style="left:13px">domain1.de</span><span style="left:78px"><i class="bar" style="width:14px"></i></span><span style="left:136px">Gemeinsame K</span><span style="left:221px">SE Keyw</span></div>
      <div class="row"><span style="left:13px">domain1.de</span><span style="left:78px"><i class="bar" style="width:22px"></i></span><span style="left:136px">Gemeinsame K</span><span style="left:221px">SE Keyw</span></div>
      <div class="row"><span style="left:13px">domain1.de</span><span style="left:78px"><i class="bar" style="width:34px"></i></span><span style="left:136px">Gemeinsame K</span><span style="left:221px">SE Keyw</span></div>
      <div class="row"><span style="left:13px">domain1.de</span><span style="left:78px"><i class="bar" style="width:48px"></i></span><span style="left:136px">Gemeinsame K</span><span style="left:221px">SE Keyw</span></div>
    </div>
  </div>
  <div class="foot"><span>Showing 1 to 5 of 9 entries</span><div class="pager"><span class="arrow"><svg width="9" height="7" viewBox="0 0 9 7"><path d="M9 3.5H1M4 0.5 1 3.5l3 3" stroke="#289cd8" stroke-width="1.2" fill="none"/></svg></span><span>1</span><span>2</span><span class="arrow"><svg width="9" height="7" viewBox="0 0 9 7"><path d="M0 3.5h8M5 0.5l3 3-3 3" stroke="#289cd8" stroke-width="1.2" fill="none"/></svg></span></div></div>
</section>

<section class="card" style="left:275px;top:866px;height:245px">
  <div class="card-head">Sternchen</div>
  <div class="search">search<svg viewBox="0 0 14 14"><circle cx="5.5" cy="5.5" r="4.3" stroke="#2a8fc4" stroke-width="2" fill="none"/><path d="M8.7 8.7l4 4" stroke="#2a8fc4" stroke-width="2.4"/></svg></div>
  <div class="table">
    <div class="thead"><span style="left:0">Name</span><span style="left:110px"><svg class="sort" viewBox="0 0 4 7"><path d="M0 3 2 0 4 3zM0 4 2 7 4 4z" fill="#fff"/></svg>Profilsiete</span><span style="left:188px"><svg class="sort" viewBox="0 0 4 7"><path d="M0 3 2 0 4 3zM0 4 2 7 4 4z" fill="#fff"/></svg>Bewertung</span></div>
    <div class="rows">
      <div class="row"><span style="left:13px">▸ lobio!</span><span style="left:134px">▸ xyz ungelost</span><span class="stars" style="left:226px">★★★★★</span></div>
      <div class="row"><span style="left:13px">▸ medilo.de</span><span style="left:134px">▸ xyz ungelost</span><span class="stars" style="left:226px">★★★★★</span></div>
      <div class="row"><span style="left:13px">▸ DIE PRAXISWAHL</span><span style="left:134px">▸ xyz ungelost</span><span class="stars" style="left:226px">★★★★★</span></div>
      <div class="row"><span style="left:13px">▸ DIE ENDVERBRAUCHER</span><span style="left:134px">▸ xyz ungelost</span><span class="stars" style="left:226px">★★★★★</span></div>
      <div class="row"><span style="left:13px">▸ DIE ENDVERBRAUCHER</span><span style="left:134px">▸ xyz ungelost</span><span class="stars" style="left:226px">★★★★★</span></div>
    </div>
  </div>
  <div class="foot"><span>Showing 1 to 5 of 9 entries</span><div class="pager"><span class="arrow"><svg width="9" height="7" viewBox="0 0 9 7"><path d="M9 3.5H1M4 0.5 1 3.5l3 3" stroke="#289cd8" stroke-width="1.2" fill="none"/></svg></span><span>1</span><span>2</span><span class="arrow"><svg width="9" height="7" viewBox="0 0 9 7"><path d="M0 3.5h8M5 0.5l3 3-3 3" stroke="#289cd8" stroke-width="1.2" fill="none"/></svg></span></div></div>
</section>
</body>
</html>
```